Label Design for Exciting Range of Nutritional Supplements

We are looking for a bright, modern design for a new range of food supplements under our new brand.

The label needs to convey a premium, high quality product with a vibrant picture of fresh fruit and clear text of what the product is.

The label needs to have a prominent colour, which matches the fruit contained in the supplement. e.g. Rasberry Ketone would have rasberry colour prominent on the label.

The chosen label will act as a template for the other labels in the range. To create the other labels, the main text can be changed and the picture of the fruit changed and the main colour altered to match the fruit.

We love the designs here: http://qrv.ly/8KTZpaw BUT our label design must not be seen to be a copy of these, they are trademarked, but must be of a unique design. I thought of the fruit morphing into a liquid drop shape dripping into a capsule to convey the fruit is contained in the capsule, but I am not sure if this would be too difficult?

Perhaps the ovel shape on our logo could encircle the label? Just ideas, I'm wide open to suggestions.

The main thing is that the label is bright, modern and attractive.

The label will wrap around a cylindrical bottle. The label size is 150mm x 72mm. The main 'focus' of the front of the logo is approximately 65mm wide in the middle of the label.

I have attached our logo in .ai and .png format. Our logo should be on the label, but we are hoping to have the label on the cap so it does not need to be too prominent on the label.

Initially the requirement is for one label: Rasberry Ketone

If the fiorst label is good, we will also require:

Garcinia Cambogia
Green Coffee
Acai Berry
African Mango

So the initial label should be the template for the others.

We will require more label designs for further products in the future.

Deliverables will need to be in Photoshop or Adobe Illustrator or Fireworks (or all three!)

```html
<!DOCTYPE html>
<html lang="en">
<head>
<meta charset="utf-8">
<title>Rasberry Ketone – Supplement Label</title>
<link rel="stylesheet" href="https://fonts.googleapis.com/css2?family=Barlow+Semi+Condensed:wght@700&family=Montserrat:wght@400;600;700&display=swap">
<style>
  :root {
    --berry-red: #e8202a;
    --brand-blue: #2b8ef0;
    --white: #ffffff;
    --ink: #1a1a1a;
    --silver-light: #e6e6e6;
    --silver-dark: #9a9a9a;
    --fruit-deep: #b3122b;
    --fruit-bright: #e83a55;
    --leaf: #3f9a3a;
  }
  html, body {
    margin: 0;
    padding: 0;
    width: 1200px;
    height: 1000px;
    overflow: hidden;
    background: var(--white);
  }
  .canvas {
    position: relative;
    width: 1200px;
    height: 1000px;
    display: flex;
    align-items: center;
    justify-content: center;
  }
  .label { display: block; }
  .label__field { fill: var(--berry-red); }
  .label__brand-tab { fill: var(--brand-blue); }
  .label__brand-name {
    font-family: "Montserrat", sans-serif;
    font-weight: 700;
    font-size: 24px;
    fill: var(--white);
    letter-spacing: 1px;
  }
  .label__ingredients {
    font-family: "Montserrat", sans-serif;
    font-weight: 400;
    font-size: 16px;
    fill: var(--white);
  }
  .label__title {
    font-family: "Barlow Semi Condensed", sans-serif;
    font-weight: 700;
    font-size: 76px;
    fill: var(--white);
  }
  .label__category {
    font-family: "Montserrat", sans-serif;
    font-weight: 600;
    font-size: 17px;
    fill: var(--white);
  }
  .label__count {
    font-family: "Montserrat", sans-serif;
    font-weight: 700;
    font-size: 14px;
    fill: var(--ink);
  }
</style>
</head>
<body>
<main class="canvas">
  <svg class="label" width="812" height="940" viewBox="60 290 510 590" xmlns="http://www.w3.org/2000/svg" aria-labelledby="label-title">
    <title id="label-title">Rasberry Ketone food supplement label</title>
    <defs>
      <linearGradient id="silver-rule" x1="0" y1="0" x2="0" y2="1">
        <stop offset="0" stop-color="var(--silver-light)"/>
        <stop offset="0.5" stop-color="var(--silver-dark)"/>
        <stop offset="1" stop-color="var(--silver-light)"/>
      </linearGradient>
      <radialGradient id="fruit-fill" cx="0.45" cy="0.45" r="0.6">
        <stop offset="0" stop-color="var(--fruit-bright)"/>
        <stop offset="0.8" stop-color="var(--fruit-deep)"/>
        <stop offset="1" stop-color="var(--fruit-deep)" stop-opacity="0"/>
      </radialGradient>
    </defs>

    <path class="label__field" d="M170,345 L550,340 C562,480 556,640 470,760 C420,830 330,862 200,862 C118,862 80,760 80,620 C80,480 110,390 170,345 Z"/>

    <path class="label__brand-tab" d="M126,307 H262 Q274,307 274,319 V378 Q274,442 210,442 H152 Q124,442 122,414 L118,322 Q118,307 126,307 Z"/>
    <text class="label__brand-name" x="196" y="392" text-anchor="middle">LUMERA</text>

    <g class="label__ingredients">
      <text x="325" y="422">PURE CAFFEINE</text>
      <text x="325" y="447">RESERVERATROL</text>
      <text x="325" y="472">RASBERRY KETONES</text>
    </g>

    <text class="label__title" x="133" y="546" textLength="372" lengthAdjust="spacingAndGlyphs">RASBERRY</text>
    <text class="label__title" x="135" y="640" textLength="362" lengthAdjust="spacingAndGlyphs">KETONE</text>

    <rect class="label__rule" x="137" y="652" width="358" height="16" fill="url(#silver-rule)"/>

    <text class="label__category" x="495" y="695" text-anchor="end">FOOD SUPPLEMENT</text>

    <ellipse class="label__fruit" role="img" aria-label="Photo of two fresh raspberries with a mint leaf" cx="215" cy="770" rx="105" ry="75" fill="url(#fruit-fill)"/>

    <text class="label__count" x="430" y="819">90 CAPSULES</text>
  </svg>
</main>
</body>
</html>
```